Free range pig farm business

We'd like a simple but elegant website for our new free range pig farm business.
Check out www.kellowridgeporkers.com.au and http://www.toravinefields.com.au/
pages:
Home
About
Shop
Contact
Target Market(s)
People who would want to find out where they could buy our pork
Industry/Entity Type
Agribusiness
Number of Pages Required
4 page
Font styles to use
Other font styles liked:
- As per our logo
Requirements
Must have
- Ability for us to update weekly with new news and photos

```html
<!DOCTYPE html>
<html lang="en">
<head>
<meta charset="utf-8">
<title>Bramblewood Pastured Pork</title>
<link href="https://fonts.googleapis.com/css2?family=Roboto:wght@300;400;500;700&display=swap" rel="stylesheet">
<style>
:root{
  --green:#6f9a1e;
  --green-dark:#3f5a17;
  --olive:#4c5f1f;
  --ink:#333333;
  --muted:#7a7a7a;
  --band:#f1f1ef;
  --white:#ffffff;
  --line:#e3e3e3;
  --sky-top:#5f8fbd;
  --sky-low:#8fb2d2;
}
*{box-sizing:border-box;margin:0;padding:0}
html,body{width:1200px;height:2548px;overflow:hidden}
body{font-family:'Roboto',Arial,sans-serif;color:var(--ink);background:var(--white);position:relative}
a{color:inherit;text-decoration:none}

.site-header{position:absolute;top:0;left:0;width:1200px;height:100px;background:var(--white);border-bottom:1px solid var(--line)}
.brand{position:absolute;left:40px;top:18px;display:flex;align-items:center;gap:10px}
.brand-dot{width:40px;height:40px;border-radius:50%;background:var(--green)}
.brand-name{font-size:13px;font-weight:700;color:var(--green-dark);line-height:1.2;width:130px;text-transform:uppercase}
.call-us{position:absolute;right:40px;top:24px;font-size:13px;font-weight:500;color:var(--green);display:flex;align-items:center;gap:6px}
.main-nav{position:absolute;right:40px;top:66px;display:flex}
.main-nav a{font-size:10px;font-weight:500;color:var(--ink);padding:6px 14px;text-transform:uppercase}
.main-nav a.active{color:var(--green);border-bottom:2px solid var(--green)}

.hero{position:absolute;top:100px;left:0;width:1200px;height:460px;background:linear-gradient(180deg,var(--sky-top) 0%,var(--sky-low) 58%,#7fae3a 74%,#4f8a22 100%)}
.hero-copy{position:absolute;left:728px;top:110px;width:380px;color:var(--white)}
.hero-title{font-size:42px;font-weight:400;margin-bottom:18px}
.hero-text{font-size:12px;line-height:1.7;margin-bottom:18px}
.btn-ghost{display:inline-block;font-size:10px;font-weight:500;border:1px solid var(--white);padding:6px 14px}
.hero-arrow{position:absolute;top:212px;width:36px;height:36px;border-radius:50%;background:rgba(255,255,255,.85);display:flex;align-items:center;justify-content:center}
.hero-arrow.prev{left:22px}.hero-arrow.next{right:22px}

.section-title{text-align:center;font-size:26px;font-weight:700;text-transform:uppercase;color:var(--ink)}
.section-title span{color:var(--green)}
.section-intro{width:640px;margin:14px auto 0;text-align:center;font-size:12px;line-height:1.7;color:var(--muted)}

.services{position:absolute;top:560px;left:0;width:1200px;height:428px}
.services .section-title{margin-top:48px}
.service-list{display:flex;justify-content:center;gap:110px;margin-top:40px}
.service{width:260px;text-align:center}
.service-icon{width:92px;height:92px;margin:0 auto;border-radius:50%;border:3px solid var(--green);padding:5px}
.service-icon div{width:100%;height:100%;border-radius:50%;background:var(--green-dark);display:flex;align-items:center;justify-content:center}
.service h3{font-size:16px;font-weight:500;margin:26px 0 10px}
.service p{font-size:11px;line-height:1.7;color:var(--muted)}

.welcome{position:absolute;top:988px;left:0;width:1200px;height:352px;background:var(--band)}
.welcome-copy{position:absolute;left:80px;top:40px;width:500px}
.welcome-copy h2{font-size:20px;font-weight:700;text-transform:uppercase;margin-bottom:16px}
.welcome-copy h2 span{color:var(--green)}
.welcome-copy p{font-size:11px;line-height:1.75;color:var(--muted);margin-bottom:14px}
.btn-solid{display:inline-block;background:var(--olive);color:var(--white);font-size:11px;font-weight:500;padding:9px 18px;text-transform:uppercase}
.welcome-art{position:absolute;left:640px;top:40px;width:280px;height:280px;background:radial-gradient(circle,#e4e4e2 0%,#f1f1ef 70%)}

.blog{position:absolute;top:1340px;left:0;width:1200px;height:592px}
.blog .section-title{margin-top:40px}
.post-list{display:flex;justify-content:center;gap:24px;margin-top:40px}
.post{width:330px}
.post-photo{width:330px;height:200px}
.post-photo.pigs{background:linear-gradient(180deg,#a9c7e0 0%,#8fb05a 55%,#6e8c3a 100%)}
.post-photo.keeper{background:linear-gradient(180deg,#d9dde0 0%,#c6b8a6 60%,#8f8a6a 100%)}
.post-photo.piglets{background:linear-gradient(180deg,#c9b79a 0%,#d8b49a 55%,#9c8a5c 100%)}
.post h3{font-size:15px;font-weight:500;margin:18px 0 8px}
.post-meta{font-size:10px;color:var(--muted);display:flex;gap:16px;margin-bottom:10px}
.post p{font-size:11px;line-height:1.7;color:var(--muted);margin-bottom:14px}
.read-more{font-size:10px;font-weight:700;color:var(--green);text-transform:uppercase}

.newsletter{position:absolute;top:1932px;left:0;width:1200px;height:288px;background:var(--band)}
.newsletter .section-title{margin-top:32px;font-size:22px}
.signup{display:flex;justify-content:center;margin-top:72px}
.signup-input{width:480px;height:44px;border:1px solid var(--line);background:var(--white);font-size:11px;color:var(--muted);padding:0 16px;display:flex;align-items:center}
.signup-btn{width:150px;height:44px;background:var(--green);color:var(--white);font-size:12px;font-weight:500;display:flex;align-items:center;justify-content:center;text-transform:uppercase}

.site-footer{position:absolute;top:2220px;left:0;width:1200px;height:280px;background:var(--white)}
.footer-brand{position:absolute;left:80px;top:40px;display:flex;flex-direction:column;align-items:center;gap:14px;width:170px}
.footer-brand .brand-dot{width:90px;height:90px}
.footer-brand .brand-name{font-size:15px;text-align:center;width:170px}
.footer-col{position:absolute;top:40px}
.footer-col h4{font-size:12px;font-weight:700;text-transform:uppercase;margin-bottom:16px}
.footer-col li{list-style:none;font-size:11px;color:var(--muted);margin-bottom:10px;display:flex;align-items:center;gap:8px}
.col-contact{left:390px;width:240px}
.col-links{left:680px;width:150px}
.col-follow{left:880px;width:240px}
.col-follow p{font-size:11px;color:var(--muted);line-height:1.7;margin-bottom:16px}
.social{display:flex;gap:8px}
.social span{width:28px;height:28px;border-radius:50%;border:1px solid #bbbbbb}

.bottom-bar{position:absolute;top:2500px;left:0;width:1200px;height:48px;background:var(--green-dark);color:#d7e3c3;font-size:11px;display:flex;align-items:center;justify-content:center}
.to-top{position:absolute;right:20px;top:12px;width:24px;height:24px;background:var(--olive)}
</style>
</head>
<body>

<header class="site-header">
  <a class="brand" href="#"><span class="brand-dot"></span><span class="brand-name">Bramblewood Pastured Pork</span></a>
  <div class="call-us">
    <svg width="14" height="14" viewBox="0 0 24 24"><path fill="#6f9a1e" d="M6.6 10.8a15.1 15.1 0 0 0 6.6 6.6l2.2-2.2a1 1 0 0 1 1-.25 11.4 11.4 0 0 0 3.6.57 1 1 0 0 1 1 1V20a1 1 0 0 1-1 1A17 17 0 0 1 3 4a1 1 0 0 1 1-1h3.5a1 1 0 0 1 1 1c0 1.25.2 2.45.57 3.57a1 1 0 0 1-.25 1z"/></svg>
    CALL US : (02) 6555 0184
  </div>
  <nav class="main-nav">
    <a class="active" href="#">Home</a><a href="#">About</a><a href="#">Service</a><a href="#">Shop</a><a href="#">Contact</a>
  </nav>
</header>

<section class="hero" role="img" aria-label="Photo of a pig standing in a green daisy-dotted pasture under a blue sky">
  <div class="hero-copy">
    <h1 class="hero-title">Pastured Pork</h1>
    <p class="hero-text">Our pigs roam open paddocks all year round, raised slowly on grass, sunshine and clean water for pork with real depth of flavour.</p>
    <a class="btn-ghost" href="#">READ MORE</a>
  </div>
  <span class="hero-arrow prev"><svg width="12" height="12" viewBox="0 0 12 12"><path d="M8 1 3 6l5 5" fill="none" stroke="#3f5a17" stroke-width="2"/></svg></span>
  <span class="hero-arrow next"><svg width="12" height="12" viewBox="0 0 12 12"><path d="m4 1 5 5-5 5" fill="none" stroke="#3f5a17" stroke-width="2"/></svg></span>
</section>

<section class="services">
  <h2 class="section-title">Our <span>Services</span></h2>
  <p class="section-intro">We raise heritage breeds outdoors with patience and care, and sell direct so you always know exactly where your pork comes from.</p>
  <div class="service-list">
    <div class="service">
      <div class="service-icon"><div><svg width="38" height="38" viewBox="0 0 24 24"><path fill="#fff" d="M20 3C9 3 4 9 4 16c0 1.2.2 2.3.5 3.3L3 21l1.4 1 1.5-1.7C7 21 8.3 21.3 9.6 21.3 17 21.3 20 14 20 3zM7 18c2-5 5-8 9-10-3 3-6 6-9 10z"/></svg></div></div>
      <h3>Free Range</h3>
      <p>Pigs live outdoors on open pasture with room to root, wallow and rest in shelter.</p>
    </div>
    <div class="service">
      <div class="service-icon"><div><svg width="40" height="40" viewBox="0 0 24 24"><path fill="#fff" d="M12 3 2 10v11h7v-6h6v6h7V10z"/></svg></div></div>
      <h3>Pig Farm</h3>
      <p>A small family farm with heritage breeds raised slowly and handled with calm and care.</p>
    </div>
    <div class="service">
      <div class="service-icon"><div><svg width="36" height="36" viewBox="0 0 24 24"><rect x="5" y="4" width="14" height="18" rx="1.5" fill="none" stroke="#fff" stroke-width="2"/><rect x="9" y="2" width="6" height="4" rx="1" fill="#fff"/><path d="m8.5 13 2.5 2.5 4.5-5" fill="none" stroke="#fff" stroke-width="2"/></svg></div></div>
      <h3>Business</h3>
      <p>Buy direct from the farm, at local markets or through our stockists across the region.</p>
    </div>
  </div>
</section>

<section class="welcome">
  <div class="welcome-copy">
    <h2>Welcome to <span>Bramblewood</span></h2>
    <p>Bramblewood is a family run farm where pigs are raised the way they should be: outdoors, on fresh pasture, with space to roam and natural shelter. We grow them slowly on a simple diet and never rush the process, so the meat is tender, well marbled and full of flavour. Every animal is cared for from birth.</p>
    <p>Find our pork at farmers markets, local butchers and restaurants, or order a mixed box direct from the farm for delivery to your door each week.</p>
    <a class="btn-solid" href="#">Read More</a>
  </div>
  <div class="welcome-art" role="img" aria-label="Pen and ink illustration of a standing pig"></div>
</section>

<section class="blog">
  <h2 class="section-title">Latest <span>Blog</span></h2>
  <p class="section-intro">News from the paddock, updated each week with fresh photos, farm stories and where to find us next.</p>
  <div class="post-list">
    <article class="post">
      <div class="post-photo pigs" role="img" aria-label="Photo of pigs grazing in a fenced green paddock"></div>
      <h3>Sed ut perspiciatis unde</h3>
      <div class="post-meta"><span>12 May 2024</span><span>3 Comments</span></div>
      <p>Spring litters are out on pasture and settling in well. Come and meet them at our open day this month.</p>
      <a class="read-more" href="#">Read More »</a>
    </article>
    <article class="post">
      <div class="post-photo keeper" role="img" aria-label="Photo of a farmer holding a piglet outside a farm shed"></div>
      <h3>Sed ut perspiciatis unde</h3>
      <div class="post-meta"><span>12 May 2024</span><span>3 Comments</span></div>
      <p>We spent the week moving sows to fresh paddocks and planting a new crop of clover for grazing.</p>
      <a class="read-more" href="#">Read More »</a>
    </article>
    <article class="post">
      <div class="post-photo piglets" role="img" aria-label="Photo of young piglets resting on straw"></div>
      <h3>Sed ut perspiciatis unde</h3>
      <div class="post-meta"><span>12 May 2024</span><span>3 Comments</span></div>
      <p>Our weaners are growing fast. Order ahead for the next batch of mixed boxes before they sell out.</p>
      <a class="read-more" href="#">Read More »</a>
    </article>
  </div>
</section>

<section class="newsletter">
  <h2 class="section-title">Subscribe to <span>Our Newsletter</span></h2>
  <p class="section-intro">Sign up for weekly farm news, new photos and the first word on fresh pork boxes and market days.</p>
  <div class="signup">
    <div class="signup-input">Enter your Email</div>
    <div class="signup-btn">Subscribe</div>
  </div>
</section>

<footer class="site-footer">
  <div class="footer-brand"><span class="brand-dot"></span><span class="brand-name">Bramblewood Pastured Pork</span></div>
  <div class="footer-col col-contact">
    <h4>Contact Us</h4>
    <ul>
      <li><svg width="12" height="12" viewBox="0 0 24 24"><path fill="#6f9a1e" d="M6.6 10.8a15.1 15.1 0 0 0 6.6 6.6l2.2-2.2a1 1 0 0 1 1-.25 11.4 11.4 0 0 0 3.6.57 1 1 0 0 1 1 1V20a1 1 0 0 1-1 1A17 17 0 0 1 3 4a1 1 0 0 1 1-1h3.5a1 1 0 0 1 1 1c0 1.25.2 2.45.57 3.57a1 1 0 0 1-.25 1z"/></svg>(02) 6555 0184</li>
      <li><svg width="12" height="12" viewBox="0 0 24 24"><path fill="#6f9a1e" d="M6.6 10.8a15.1 15.1 0 0 0 6.6 6.6l2.2-2.2a1 1 0 0 1 1-.25 11.4 11.4 0 0 0 3.6.57 1 1 0 0 1 1 1V20a1 1 0 0 1-1 1A17 17 0 0 1 3 4a1 1 0 0 1 1-1h3.5a1 1 0 0 1 1 1c0 1.25.2 2.45.57 3.57a1 1 0 0 1-.25 1z"/></svg>(02) 6555 0192</li>
      <li><svg width="12" height="12" viewBox="0 0 24 24"><rect x="2" y="5" width="20" height="14" fill="none" stroke="#6f9a1e" stroke-width="2"/><path d="m2 5 10 8 10-8" fill="none" stroke="#6f9a1e" stroke-width="2"/></svg>hello@bramblewoodpork.com.au</li>
      <li><svg width="12" height="12" viewBox="0 0 24 24"><path fill="#6f9a1e" d="M12 2a7 7 0 0 0-7 7c0 5 7 13 7 13s7-8 7-13a7 7 0 0 0-7-7zm0 9.5A2.5 2.5 0 1 1 12 6.5a2.5 2.5 0 0 1 0 5z"/></svg>14 Paddock Road, Kellow Creek NSW</li>
    </ul>
  </div>
  <div class="footer-col col-links">
    <h4>Quick Links</h4>
    <ul>
      <li>› Home</li><li>› About</li><li>› Service</li><li>› Shop</li><li>› Contact</li>
    </ul>
  </div>
  <div class="footer-col col-follow">
    <h4>Follow Us</h4>
    <p>Follow the farm for daily photos and news from the paddocks.</p>
    <div class="social"><span></span><span></span><span></span><span></span><span></span></div>
  </div>
</footer>

<div class="bottom-bar">© Copyright 2024 Bramblewood Pork. All Rights Reserved.<span class="to-top"></span></div>

</body>
</html>
```